Design Project for Digital Recruitment Business

I am launching a new website in the Digital Marketing Recruitment space here in the UK.We are a start up so this very much phase 1 with our web offering.

Key points:

- I think it will be aproximately 5- 8 pages

- I am looking for wordpress(open on this)) design and coding/ development.

- It really is going to be a brochure site on the whole so don't expect any huge integration. I would like an RSS feed to publish our jobs on our site. I can get the code for that from my recruitment database partner Quillpost, all i will need is a blank page for that section?.Parley net,chirrup etc as well.

-I already have the logo.(See attached)which you guys delivered brilliantly on :-)

some reference sites I like the look of: http://www.orbitvale.example.co.uk http://www.ratchethouse.example.com/ http://www.webmavens.example.co.uk/

The menu bar on these sites are good, the language is good.I want contemporary and professional.It needs to connect to the viewer.
WE are in the social media space so that needs to fit/blend eg parleynet,GS.

SUGGESTED APPROACH
So I guess the best starting point would be to just submit a home page design so i can judge the styles I like best.Then the finalists of that round can submit another section of the website to see the consistency in terms of look and feel. I will then pick someone to work one on one with to complete the design and do the coding. That way no one gets to waste valuable time and energy :-)

Feel free to ping me questions
Updates

Reason: Hello All, I am going to extend by a few days. I have been inundated with work.However I Plan to look at all your designs this week end and respond to all your Queries. Thanks for your Patience.

Hi guys

here is a little more about us

We know that the career success of the candidates we place can have a great impact on the success of your business. We have built a network of talented industry professionals and an extensive knowledge of the market and its changing trends. We focus on career management,advice and consultancy.With over 30 years experience in our team we feel confident we can deliver. Our specialisms are Creative and Design,Digital Marketing,Editorial and Content,User Experience,and Technology related to building Websites.

In today's world of continually adapting,surviving and thriving we recognise that you rise and fall by the people you hire.That is why an expert  is required to help find those people in business critical roles. So if your online Marketing strategy is behind the times or your website traffic is poor for example we can help find people on a contract and permanent basis to bridge the gap in you marketing and E-commerce team. Pixel Scouts are specialists in these areas and offer a consultative approach to working with your business. If your business grows as a result of the people you recruited through us we could not be happier. Honest,straightforward,professional.

In terms of home page the Menu bar is 4-5 topics at most. 90% of the traffic to this website will be Candidates so Jobs will be the best content along with the 6 skill sets/categories and everything social after that.Very like Ratchet website I mentioned in the Brief. A couple of you are on the right tracks.
Hope this helps for now. I feel confident I can pick from one of you.

Kind regards

Martin

Soory one other thing,

RE; Images

People are tricky to do on Recruitment websites as its very PC and they dont look real enough.Animations of people are better in my humble opinion...

open to ideas/options

Thanks

Target Market(s)

marketeers,designers,ecommerce folks.

Industry/Entity Type

Business

Requirements
Must have
• open at this stage but obviously the logo design colours must sync with the overall look and feel.GS,chirrup,mingle+ must be dominant

```html
<!DOCTYPE html>
<html lang="en">
<head>
<meta charset="utf-8">
<title>Pixel Scouts — Digital Recruitment</title>
<link href="https://fonts.googleapis.com/css2?family=PT+Sans:ital,wght@0,400;0,700;1,400&family=PT+Sans+Narrow&family=Oswald:wght@300;400&family=Noto+Serif:ital@1&display=swap" rel="stylesheet">
<style>
  :root {
    --nav-bg: #2b2b2b;
    --nav-text: #e6e6e6;
    --orange: #f26a10;
    --orange-dark: #e04e00;
    --purple: #2e1a87;
    --body-text: #666666;
    --dark-text: #222222;
    --rule-grey: #8a8a8a;
    --hero-light: #f7f7f7;
    --hero-mid: #e4e4e4;
    --footer-text: #a8a8a8;
  }
  * { margin: 0; padding: 0; box-sizing: border-box; }
  html, body { width: 1200px; height: 891px; overflow: hidden; }
  body { position: relative; background: #fff; font-family: "PT Sans", sans-serif; color: var(--body-text); }
  h2, h3 { font-weight: 400; }

  .main-nav { position: absolute; left: 0; top: 0; width: 1200px; height: 50px; background: var(--nav-bg); border-bottom: 4px solid var(--rule-grey); }
  .main-nav a { position: absolute; top: 16px; transform: translateX(-50%); font-size: 11px; letter-spacing: 1.6px; text-transform: uppercase; color: var(--nav-text); text-decoration: none; text-shadow: 0 1px 1px #000; white-space: nowrap; }
  .main-nav a.is-active { color: var(--orange); }

  .hero { position: absolute; left: 0; top: 50px; width: 1200px; height: 290px; background: radial-gradient(ellipse at 45% 40%, #ffffff 0%, var(--hero-light) 40%, var(--hero-mid) 100%); border-bottom: 4px solid #dcdcdc; }
  .hero-photo { position: absolute; left: 200px; top: 8px; width: 400px; height: 278px;
    background:
      radial-gradient(ellipse 42% 70% at 30% 62%, rgba(40,40,40,.75) 0%, rgba(70,70,70,.45) 45%, rgba(120,120,120,0) 100%),
      radial-gradient(ellipse 40% 72% at 68% 60%, rgba(190,190,190,.55) 0%, rgba(215,215,215,.3) 50%, rgba(235,235,235,0) 100%); }
  .hero-brand { position: absolute; left: 683px; top: 116px; display: flex; align-items: center; gap: 8px; font-size: 30px; font-weight: 700; color: var(--orange); letter-spacing: -0.5px; }
  .hero-brand .brand-dot { width: 26px; height: 26px; border-radius: 50%; background: var(--orange); }
  .hero-title { position: absolute; left: 683px; top: 170px; font-size: 12px; letter-spacing: 1px; color: var(--purple); text-transform: uppercase; }
  .hero-text { position: absolute; left: 683px; top: 193px; width: 380px; font-size: 11px; line-height: 16px; letter-spacing: .6px; color: var(--body-text); }
  .hero-button { position: absolute; left: 682px; top: 240px; width: 74px; height: 29px; border-radius: 3px; border: 1px solid var(--orange-dark); background: linear-gradient(#ff7a1f, var(--orange-dark)); color: #fff; font-size: 11px; display: flex; align-items: center; justify-content: center; gap: 5px; text-decoration: none; }

  .services { position: absolute; left: 0; top: 360px; width: 1200px; }
  .service { position: absolute; width: 190px; transform: translateX(-50%); text-align: center; }
  .service-icon { width: 100px; height: 96px; margin: 8px auto 0; border-radius: 10px; background: linear-gradient(#8e8e8e, #3c3c3c); }
  .service-icon.is-round { border-radius: 50%; background: radial-gradient(circle at 35% 30%, #f0f0f0, #8a8a8a 75%); }
  .service-icon.is-paper { width: 70px; background: linear-gradient(#fafafa, #d6d6d6); border: 1px solid #ccc; border-radius: 2px; }
  .service-shadow { width: 150px; height: 12px; margin: 6px auto 0; border-radius: 50%; background: radial-gradient(ellipse, rgba(0,0,0,.28), rgba(0,0,0,0) 70%); }
  .service-title { margin-top: 18px; font-size: 12px; letter-spacing: 1px; color: var(--purple); text-transform: uppercase; }
  .service-text { margin-top: 9px; font-size: 10.5px; line-height: 19px; letter-spacing: .6px; }
  .service-more { display: inline-block; margin-top: 7px; font-size: 10px; font-weight: 700; letter-spacing: .6px; color: var(--dark-text); text-decoration: none; }

  .intro-title { position: absolute; left: 173px; top: 655px; font-family: "Oswald", sans-serif; font-weight: 300; font-size: 19px; letter-spacing: 1.2px; color: #333; text-transform: uppercase; }
  .intro-text { position: absolute; left: 175px; top: 694px; width: 550px; font-size: 10.5px; line-height: 26px; letter-spacing: .6px; }
  .link-list { position: absolute; left: 771px; top: 689px; list-style: none; }
  .link-list li { display: flex; align-items: center; gap: 10px; height: 32.5px; }
  .link-list li::before { content: ""; width: 7px; height: 7px; background: var(--orange); }
  .link-list a { font-family: "Noto Serif", Georgia, serif; font-style: italic; font-size: 10.5px; letter-spacing: .8px; color: var(--purple); }

  .site-footer { position: absolute; left: 0; top: 846px; width: 1200px; height: 45px; background: var(--nav-bg); border-top: 4px solid var(--rule-grey); font-family: "PT Sans Narrow", sans-serif; font-size: 11px; }
  .site-footer a, .site-footer .copyright { position: absolute; top: 15px; color: var(--footer-text); text-decoration: none; }
  .site-footer a.is-active { color: var(--orange); }
  .site-footer .copyright { right: 171px; }
  .site-footer .copyright span { color: var(--orange); }
</style>
</head>
<body>
  <nav class="main-nav">
    <a class="is-active" href="#" style="left:220px">Home</a>
    <a href="#" style="left:349px">Candidates</a>
    <a href="#" style="left:489px">Clients</a>
    <a href="#" style="left:611px">Jobs</a>
    <a href="#" style="left:720px">Blog</a>
    <a href="#" style="left:839px">About us</a>
    <a href="#" style="left:974px">Contact</a>
  </nav>

  <header class="hero">
    <div class="hero-photo" role="img" aria-label="Black and white photo of two smiling professionals, a man and a woman, arms crossed"></div>
    <div class="hero-brand"><span class="brand-dot"></span>Pixel Scouts</div>
    <h2 class="hero-title">Donec faucibus</h2>
    <p class="hero-text">Fusce vulputate pharetra elit, vitae pulvinar tellus sollicitudin ultrices. Morbi cursus, dolor in bibendum laoreet, libero mauris</p>
    <a class="hero-button" href="#">Go
      <svg width="5" height="7" viewBox="0 0 5 7"><path d="M0 0L5 3.5L0 7Z" fill="#fff"/></svg>
    </a>
  </header>

  <section class="services">
    <div class="service" style="left:255px">
      <div class="service-icon" role="img" aria-label="Dark grey person bust icon"></div>
      <div class="service-shadow"></div>
      <h3 class="service-title">Morbi cursus</h3>
      <p class="service-text">Vitae pulvinar tellus sollicitudin ultrices. Morbi cursus, dolor in bibendum laoreet, libero mauri</p>
      <a class="service-more" href="#">read more</a>
    </div>
    <div class="service" style="left:483px">
      <div class="service-icon" role="img" aria-label="Monitor with magnifying glass icon"></div>
      <div class="service-shadow"></div>
      <h3 class="service-title">Morbi cursus</h3>
      <p class="service-text">Vitae pulvinar tellus sollicitudin ultrices. Morbi cursus, dolor in bibendum laoreet, libero mauri</p>
      <a class="service-more" href="#">read more</a>
    </div>
    <div class="service" style="left:717px">
      <div class="service-icon is-round" role="img" aria-label="Silver globe icon"></div>
      <div class="service-shadow"></div>
      <h3 class="service-title">Morbi cursus</h3>
      <p class="service-text">Vitae pulvinar tellus sollicitudin ultrices. Morbi cursus, dolor in bibendum laoreet, libero mauri</p>
      <a class="service-more" href="#">read more</a>
    </div>
    <div class="service" style="left:944px">
      <div class="service-icon is-paper" role="img" aria-label="Document with pen icon"></div>
      <div class="service-shadow"></div>
      <h3 class="service-title">Morbi cursus</h3>
      <p class="service-text">Vitae pulvinar tellus sollicitudin ultrices. Morbi cursus, dolor in bibendum laoreet, libero mauri</p>
      <a class="service-more" href="#">read more</a>
    </div>
  </section>

  <h2 class="intro-title">Laced diam ipsu laci</h2>
  <p class="intro-text">Fusce vulputate pharetra elit, vitae pulvinar tellus sollicitudin ultrices. Morbi cursus, dolor in bibendum laoreet, libero mauris consectetur mi, placerat accumsan nulla tortor a ligula. Sed egestas egestas mauris, non porta nunc vestibulum quis. Aliquam tortor sem, gravida nec convallis sed, porttitor at odio. Donec vestibulum suscipit tincidunt. Pellentesque auctor odio eu mi</p>
  <ul class="link-list">
    <li><a href="#">Vel diam ipsum, a lacinia sem uis a sagit-</a></li>
    <li><a href="#">Tis laoreet justo vel facilisis neque ollo</a></li>
    <li><a href="#">Cosectetur in ed tristique metus vulpure</a></li>
  </ul>

  <footer class="site-footer">
    <a class="is-active" href="#" style="left:171px">Home</a>
    <a href="#" style="left:230px">Menu</a>
    <a href="#" style="left:284px">About</a>
    <a href="#" style="left:337px">Contact</a>
    <p class="copyright">Copyright © 2012 <span>Pixel Scouts</span> | All rights reserved</p>
  </footer>
</body>
</html>
```